Industrial Professional Business Card Design (Vantrel Systems)

Would like professional looking business cards. Not too busy leaning towards minimal. Should have a slogan like:
"Industrial Automation and Control".

We are a tech company that programs industrial PLC computers. We also develop custom hardware solutions. Please use the logo for inspiration.

Target Market(s)

Mining, industrial, processing, automation, factory

Industry/Entity Type

Engineering

Contact Information for Business Card

Name, phone, email, website. job title.

Font styles to use
Other font styles liked:
• droid sans

Requirements
Must have
• Use colours that go well with the logo. Not too busy design.

```html
<!DOCTYPE html>
<html lang="en">
<head>
<meta charset="UTF-8">
<title>Vantrel Systems — Business Card</title>
<link rel="stylesheet" href="https://fonts.googleapis.com/css2?family=Roboto:wght@400;500;700&display=swap">
<style>
  :root {
    --backdrop: #cbcbcb;
    --card-white: #ffffff;
    --navy: #1e4a70;
    --orange: #f26a21;
    --ink: #3d3d3d;
    --muted: #555a60;
  }
  * { margin: 0; padding: 0; box-sizing: border-box; }
  html, body {
    width: 1200px;
    height: 1200px;
    overflow: hidden;
    background: var(--backdrop);
    font-family: "Roboto", Arial, sans-serif;
  }
  .sheet { position: relative; width: 1200px; height: 1200px; }

  .card {
    position: absolute;
    left: 204px;
    width: 786px;
    height: 446px;
    border-radius: 22px;
    overflow: hidden;
  }
  .card--front { top: 134px; background: var(--card-white); }
  .card--back  { top: 622px; background: var(--navy); }

  /* Front: brand block */
  .brand {
    position: absolute;
    left: 0;
    width: 396px;
    top: 190px;
    display: flex;
    align-items: center;
    justify-content: center;
    gap: 12px;
  }
  .brand__dot {
    width: 18px; height: 18px;
    border-radius: 50%;
    background: var(--orange);
    flex: none;
  }
  .brand__name {
    font-size: 34px;
    font-weight: 500;
    color: var(--navy);
    letter-spacing: 0.2px;
    white-space: nowrap;
  }

  .divider {
    position: absolute;
    left: 396px;
    top: 128px;
    width: 3px;
    height: 192px;
    background: var(--orange);
  }

  /* Front: contact block */
  .contact {
    position: absolute;
    left: 434px;
    top: 125px;
  }
  .contact__name {
    font-size: 34px;
    font-weight: 700;
    color: var(--navy);
    letter-spacing: 0.5px;
    line-height: 1.1;
  }
  .contact__title {
    margin-top: 6px;
    font-size: 15px;
    font-weight: 400;
    color: var(--muted);
    letter-spacing: 0.3px;
  }
  .contact__rule {
    width: 17px;
    height: 2px;
    background: var(--orange);
    margin-top: 20px;
    margin-bottom: 22px;
  }
  .contact__list { list-style: none; }
  .contact__item {
    display: flex;
    align-items: center;
    gap: 13px;
    height: 31px;
    font-size: 18px;
    color: var(--ink);
  }
  .contact__icon { width: 20px; height: 20px; flex: none; }
  .contact__accent { color: var(--orange); }

  /* Back */
  .back-brand {
    position: absolute;
    inset: 0;
    display: flex;
    align-items: center;
    justify-content: center;
    gap: 22px;
  }
  .back-brand__dot {
    width: 40px; height: 40px;
    border-radius: 50%;
    background: var(--orange);
    flex: none;
  }
  .back-brand__name {
    font-size: 72px;
    font-weight: 500;
    color: var(--card-white);
    white-space: nowrap;
  }
</style>
</head>
<body>
<main class="sheet">

  <section class="card card--front" aria-label="Business card front">
    <div class="brand">
      <span class="brand__dot"></span>
      <span class="brand__name">Vantrel Systems</span>
    </div>

    <div class="divider"></div>

    <div class="contact">
      <h1 class="contact__name">MAREN OKAFOR</h1>
      <p class="contact__title">CREATIVE CO-OPPRETOR</p>
      <div class="contact__rule"></div>
      <ul class="contact__list">
        <li class="contact__item">
          <svg class="contact__icon" viewBox="0 0 24 24" aria-hidden="true">
            <path fill="var(--navy)" d="M6.6 10.8c1.4 2.8 3.8 5.1 6.6 6.6l2.2-2.2c.3-.3.7-.4 1-.2 1.1.4 2.3.6 3.6.6.6 0 1 .4 1 1V20c0 .6-.4 1-1 1C10.6 21 3 13.4 3 4c0-.6.4-1 1-1h3.5c.6 0 1 .4 1 1 0 1.3.2 2.5.6 3.6.1.3 0 .7-.2 1z"/>
            <path fill="none" stroke="var(--navy)" stroke-width="1.6" stroke-linecap="round" d="M14 3.5a6.5 6.5 0 0 1 6.5 6.5M14 7a3 3 0 0 1 3 3"/>
          </svg>
          <span>+81 555 010 274</span>
        </li>
        <li class="contact__item">
          <svg class="contact__icon" viewBox="0 0 24 24" aria-hidden="true">
            <rect x="2.5" y="5" width="19" height="14" rx="1" fill="var(--navy)"/>
            <path d="M3 6l9 7 9-7" fill="none" stroke="#fff" stroke-width="1.6"/>
          </svg>
          <span>info@vantrelmail.com</span>
        </li>
        <li class="contact__item">
          <svg class="contact__icon" viewBox="0 0 24 24" aria-hidden="true">
            <circle cx="12" cy="12" r="9.5" fill="none" stroke="var(--navy)" stroke-width="1.8"/>
            <path fill="var(--navy)" d="M7 7.5c1.5-.5 3 .3 3 1.8s-2 1.2-2 2.7 1.5 2 1.5 3.5-1.2 2-2 2.5C5.5 16 4.5 13 5 10.5zM14 5c2 .5 4 2.3 4.6 4.5-1.2.4-2.4-.3-3.4.5s.2 2.6-.8 3.5-2.2-.6-2.6-1.8.6-2 .2-3.4S13 5.6 14 5z"/>
          </svg>
          <span>www.<span class="contact__accent">vantrelsystems</span>.com</span>
        </li>
      </ul>
    </div>
  </section>

  <section class="card card--back" aria-label="Business card back">
    <div class="back-brand">
      <span class="back-brand__dot"></span>
      <span class="back-brand__name">Vantrel Systems</span>
    </div>
  </section>

</main>
</body>
</html>
```